Create modern and sleek business card for luxury real estate company

We're a "boutique" real estate office looking for a design that gets across a highly modern luxury brand. Blacks and whites are probably the best colors unless we try a silver foil for the logo. I've attached a version of our current logo here. I'd like to swap out the current font on there with Gotham Light Regular.

I'm looking to have one side of the card have the logo with the space for our agents info on the other side.

Target Market(s)

Young professionals in a "luxury" headspace

Industry/Entity Type

Real estate

Contact Information for Business Card

A place for agent name, cell number, website. The slogan "Simply Refining the Home Hunt".

Font styles to use
Other font styles liked:
• Gotham Regular

Colors

Designer to choose only greyscale colors for use in the design.

Requirements
Must have
• Matte black as the background color. Clean lines and use of contrast. A specific design aspect that will use silver foil.
Nice to have
• Up in the air on integrating a QR code
Should not have
• Any houses or other real estate related design (ex: a clip art house)

```html
<!DOCTYPE html>
<html lang="en">
<head>
<meta charset="UTF-8">
<title>Halden Realty — Business Card</title>
<link rel="stylesheet" href="https://fonts.googleapis.com/css2?family=Lato:wght@400;700&family=Montserrat:wght@300;400&display=swap">
<style>
  :root {
    --page: #ffffff;
    --card: #1c1d1f;
    --silver: #cfcfcf;
    --tagline: #8a8a8a;
    --white: #ffffff;
    --qr-label: #333333;
  }
  html, body {
    margin: 0;
    padding: 0;
    width: 1200px;
    height: 1200px;
    overflow: hidden;
    background: var(--page);
  }
  .canvas {
    position: relative;
    width: 1200px;
    height: 1200px;
  }
  .card {
    position: absolute;
    left: 146px;
    width: 903px;
    height: 508px;
    background: var(--card);
  }
  .card--front { top: 73px; }
  .card--back { top: 613px; }

  .brand-circle {
    position: absolute;
    left: 193px;
    top: 167px;
    width: 140px;
    height: 140px;
    border: 3px solid var(--silver);
    border-radius: 50%;
  }
  .brand-line {
    position: absolute;
    left: 379px;
    margin: 0;
    font-family: "Montserrat", sans-serif;
    font-weight: 300;
    font-size: 68px;
    line-height: 84px;
    letter-spacing: 2px;
    color: var(--silver);
    white-space: nowrap;
  }
  .brand-line--top { top: 154px; }
  .brand-line--bottom { top: 238px; }
  .brand-rule {
    position: absolute;
    left: 368px;
    top: 236px;
    width: 340px;
    height: 2px;
    background: var(--silver);
  }
  .tagline {
    position: absolute;
    left: 0;
    width: 903px;
    top: 336px;
    margin: 0;
    text-align: center;
    font-family: "Montserrat", sans-serif;
    font-weight: 400;
    font-size: 16px;
    line-height: 22px;
    letter-spacing: 8.2px;
    color: var(--tagline);
    white-space: nowrap;
  }

  .qr-slot {
    position: absolute;
    left: 177px;
    top: 167px;
    width: 173px;
    height: 173px;
    background: var(--white);
    display: flex;
    align-items: center;
    justify-content: center;
    font-family: "Montserrat", sans-serif;
    font-size: 18px;
    color: var(--qr-label);
  }
  .agent-name {
    position: absolute;
    left: 373px;
    top: 153px;
    margin: 0;
    font-family: "Lato", sans-serif;
    font-weight: 700;
    font-size: 38px;
    color: var(--white);
    white-space: nowrap;
  }
  .contact-list {
    position: absolute;
    left: 375px;
    top: 227px;
    margin: 0;
    padding: 0;
    list-style: none;
  }
  .contact-item {
    display: flex;
    align-items: center;
    height: 42px;
    font-family: "Lato", sans-serif;
    font-size: 30px;
    color: var(--white);
    white-space: nowrap;
  }
  .contact-icon {
    width: 22px;
    height: 22px;
    margin-right: 23px;
    flex: none;
  }
</style>
</head>
<body>
<div class="canvas">
  <section class="card card--front">
    <div class="brand-circle"></div>
    <h1 class="brand-line brand-line--top">HALDEN</h1>
    <div class="brand-rule"></div>
    <p class="brand-line brand-line--bottom">REALTY</p>
    <p class="tagline">SIMPLY REFINING THE HOME HUNT</p>
  </section>

  <section class="card card--back">
    <div class="qr-slot">QR code</div>
    <h2 class="agent-name">PERSON NAME</h2>
    <ul class="contact-list">
      <li class="contact-item">
        <svg class="contact-icon" viewBox="0 0 26 26" fill="none" stroke="#fff" stroke-width="2.4">
          <rect x="7" y="2" width="12" height="22" rx="2"/>
          <circle cx="13" cy="19" r="1.4" fill="#fff" stroke="none"/>
        </svg>
        000 3157 8842
      </li>
      <li class="contact-item">
        <svg class="contact-icon" viewBox="0 0 26 26" fill="none" stroke="#fff" stroke-width="2">
          <rect x="2" y="6" width="22" height="14"/>
          <path d="M2 6 L13 15 L24 6 M2 20 L10 12 M24 20 L16 12"/>
        </svg>
        info@haldenrealty.com
      </li>
      <li class="contact-item">
        <svg class="contact-icon" viewBox="0 0 26 26" fill="none" stroke="#fff" stroke-width="2">
          <circle cx="13" cy="13" r="10"/>
          <ellipse cx="13" cy="13" rx="4.5" ry="10"/>
          <path d="M3 13 H23 M5 8 H21 M5 18 H21"/>
        </svg>
        www.haldenrealty.com
      </li>
    </ul>
  </section>
</div>
</body>
</html>
```